Post Card (5x7) - Pre-foreclosure Image - Harbor Path Partners

(Two-Sided Post Card)
FACING FORECLOSURE? YOU STILL HAVE OPTIONS.
If you’re behind on payments or at risk of foreclosure, you’re not alone—and it’s not too late to take action.
We help homeowners:
• Explore options to stay in their home
• Stop or delay foreclosure
• Sell quickly for a fair price if needed
No pressure. No obligation. Just real solutions tailored to your situation.
Call - (240) 558-2094
Email - marcus@hpbllc-mail.com
Harbor Path Partners LLC
7200 Bramwick Lane, Ellicott City, MD 21043
**Marcus Fennimore is a Licensed Realtor with Copperleaf Homes Realty in Bethesda, Maryland.
(Leave room for mailing address, return address & postage)
Target Market(s)
Distressed Homeowners
Industry/Entity Type
Real Estate

```html
<!DOCTYPE html>
<html lang="en">
<head>
<meta charset="utf-8">
<title>Harbor Path Partners – Pre-foreclosure Postcard</title>
<link href="https://fonts.googleapis.com/css2?family=Bebas+Neue&family=Poppins:wght@400;500;600&display=swap" rel="stylesheet">
<style>
  :root{
    --backdrop:#ffc400;
    --gold:#b38b00;
    --ink:#000;
    --paper:#fff;
    --rule:#c8c8c8;
    --soft-band:#f0f0f0;
  }
  *{box-sizing:border-box;margin:0;padding:0}
  html,body{width:863px;height:1200px;overflow:hidden}
  body{background:var(--backdrop);position:relative;font-family:"Poppins",sans-serif;color:var(--ink)}
  .abs{position:absolute}
  .display{font-family:"Bebas Neue",sans-serif;line-height:1;letter-spacing:0;font-weight:400;white-space:nowrap}

  /* Front */
  .front{left:105px;top:100px;width:653px;height:467px;background:var(--ink);overflow:hidden}
  .brand-panel{left:0;top:0;width:266px;height:129px;background:var(--paper);display:flex;align-items:center;justify-content:center;gap:10px}
  .brand-mark{width:22px;height:22px;background:var(--ink);flex:none}
  .brand-name{font-weight:600;font-size:17px;line-height:1.15;color:var(--ink);letter-spacing:1px;text-transform:uppercase}
  .skyline-photo{left:266px;top:0;width:387px;height:129px;background:linear-gradient(180deg,#4a5a6a 0%,#a0673a 45%,#e99a3a 62%,#2a1c14 80%,#0d0b0a 100%)}
  .gold-band{left:0;top:129px;width:653px;height:8px;background:var(--gold)}
  .headline{left:40px;top:150px;font-size:82px;color:var(--gold)}
  .subhead{left:40px;top:221px;font-size:33px;color:var(--paper)}
  .reassure{left:305px;top:225px;width:306px;height:25px;background:var(--gold);border-radius:3px;color:var(--paper);font-size:8.4px;font-weight:600;line-height:10.5px;padding:2px 5px;letter-spacing:-0.05px}
  .benefit-area{left:0;top:313px;width:392px;height:92px;background:var(--paper)}
  .soft-band{left:0;top:315px;width:392px;height:10px;background:var(--soft-band)}
  .benefit{width:118px;text-align:center;top:272px}
  .benefit .ring{width:96px;height:96px;border-radius:50%;background:var(--paper);margin:0 auto;display:flex;align-items:center;justify-content:center}
  .benefit .disc{width:84px;height:84px;border-radius:50%;background:var(--ink);display:flex;align-items:center;justify-content:center}
  .benefit .disc.gold{background:var(--gold)}
  .benefit p{font-size:10.5px;line-height:11.5px;color:#111;margin-top:4px}
  .house-photo{left:392px;top:275px;width:261px;height:130px;background:linear-gradient(180deg,#9aa7b5 0%,#7a6a5e 45%,#8b7462 70%,#6f7d55 100%)}
  .cta-bar{left:0;top:405px;width:653px;height:62px;background:var(--ink)}
  .cta-call{left:42px;top:16px;font-size:32px;color:var(--paper)}
  .cta-call span{color:var(--gold)}
  .cta-mail{left:406px;top:20px;display:flex;align-items:center;gap:10px;color:var(--paper);font-size:14.5px;font-weight:500;white-space:nowrap}

  /* Back */
  .back{left:105px;top:633px;width:653px;height:466px;background:var(--paper);overflow:hidden}
  .message-panel{left:0;top:0;width:326px;height:466px;background:var(--ink)}
  .city-strip{left:326px;top:0;width:69px;height:466px;background:linear-gradient(180deg,#5a6270 0%,#9a6a44 30%,#2a1e18 55%,#3b2b22 80%,#5a3a24 100%)}
  .back-title{left:39px;top:36px;font-size:49px;line-height:45px;color:var(--gold)}
  .back-body{left:39px;top:139px;width:274px;font-size:11.5px;line-height:13.5px;color:var(--paper);text-align:justify}
  .tag{left:39px;height:29px;font-size:26px;padding:3px 0 0 6px;border-radius:0 15px 15px 0}
  .tag.light{background:var(--paper);color:var(--ink)}
  .tag.gold{background:var(--gold);color:var(--ink)}
  .licence{left:39px;top:305px;width:276px;font-size:10.5px;line-height:13px;color:var(--paper)}
  .back-call{left:39px;top:359px;font-size:31px;color:var(--paper)}
  .back-call span{color:var(--gold)}
  .contact-pill{top:392px;height:23px;display:flex;align-items:center;gap:6px;font-weight:500;white-space:nowrap}
  .contact-pill.web{left:39px;width:126px;background:var(--paper);color:var(--ink);border-radius:3px 0 0 3px;padding-left:10px;font-size:9.5px}
  .contact-pill.mail{left:168px;width:146px;background:var(--gold);color:var(--paper);border-radius:0 3px 3px 0;padding-left:6px;font-size:8.6px;gap:5px}
  .address{left:40px;top:419px;font-size:12.5px;color:var(--paper);white-space:nowrap}
  .stamp-box{left:523px;top:31px;width:95px;height:95px;border:1px solid var(--rule)}
  .address-line{left:438px;width:180px;height:1px;background:var(--rule)}
  .back-brand{left:475px;top:400px;display:flex;align-items:center;gap:7px}
  .back-brand .brand-mark{width:13px;height:13px}
  .back-brand .brand-name{font-size:10px}
</style>
</head>
<body>

<section class="abs front" aria-label="Postcard front">
  <div class="abs brand-panel">
    <span class="brand-mark"></span>
    <span class="brand-name">Harbor Path<br>Partners LLC</span>
  </div>
  <div class="abs skyline-photo" role="img" aria-label="City skyline silhouetted against a sunset sky"></div>
  <div class="abs gold-band"></div>

  <h1 class="abs display headline">Facing Foreclosure?</h1>
  <h2 class="abs display subhead">You Still Have Options</h2>
  <p class="abs reassure">If you’re behind on payments or at risk of foreclosure, you’re not alone—and it’s not too late to take action.</p>

  <div class="abs benefit-area"></div>
  <div class="abs soft-band"></div>

  <div class="abs benefit" style="left:29px">
    <div class="ring"><div class="disc">
      <svg width="48" height="48" viewBox="0 0 48 48" fill="none" stroke="#fff" stroke-width="2.6" stroke-linejoin="round">
        <path d="M6 23 L24 7 L42 23"/><path d="M11 19 V41 H37 V19"/><path d="M20 41 V31 A4 4 0 0 1 28 31 V41"/><path d="M13 14 V8 H17 V11"/>
      </svg>
    </div></div>
    <p>Explore Options to<br>Stay in Their Home</p>
  </div>
  <div class="abs benefit" style="left:147px">
    <div class="ring"><div class="disc gold">
      <svg width="48" height="50" viewBox="0 0 48 50" fill="none" stroke="#fff" stroke-width="2.4" stroke-linejoin="round" stroke-linecap="round">
        <path d="M24 4 L42 10 V24 C42 35 34 42 24 46 C14 42 6 35 6 24 V10 Z"/>
        <path d="M24 10 L36 14 V24 C36 32 31 37 24 40 C17 37 12 32 12 24 V14 Z"/>
        <path d="M18 24 L22 28 L30 20"/>
      </svg>
    </div></div>
    <p>Stop or Delay<br>Foreclosure</p>
  </div>
  <div class="abs benefit" style="left:265px">
    <div class="ring"><div class="disc">
      <svg width="58" height="44" viewBox="0 0 58 44" fill="none" stroke="#fff" stroke-width="2.4" stroke-linejoin="round" stroke-linecap="round">
        <path d="M3 12 L12 4 L20 13 L11 21 Z"/><path d="M55 12 L46 4 L38 13 L47 21 Z"/>
        <path d="M20 13 L28 10 L38 13"/><path d="M28 10 L22 18 C24 20 27 19 30 16 L41 26"/>
        <path d="M11 21 L27 36 C29 38 32 37 33 35 L41 26 L47 21"/>
        <circle cx="18" cy="28" r="2.5"/><circle cx="22" cy="32" r="2.5"/><circle cx="26" cy="36" r="2.5"/>
      </svg>
    </div></div>
    <p>Sell Quickly for a<br>Fair Price if Needed</p>
  </div>

  <div class="abs house-photo" role="img" aria-label="Stone house with a red foreclosure for-sale sign on the lawn"></div>

  <div class="abs cta-bar">
    <p class="abs display cta-call">Call Now Today! <span>(240) 558-2094</span></p>
    <p class="abs cta-mail">
      <svg width="22" height="17" viewBox="0 0 22 17" fill="none" stroke="#fff" stroke-width="2.2" stroke-linejoin="round"><rect x="1.5" y="1.5" width="19" height="14" rx="3"/><path d="M3 4 L11 10 L19 4"/></svg>
      marcus@hpbllc-mail.com
    </p>
  </div>
</section>

<section class="abs back" aria-label="Postcard back">
  <div class="abs message-panel">
    <h2 class="abs display back-title">Real Solutions.<br>No Pressure.</h2>
    <p class="abs back-body">We understand how overwhelming foreclosure can feel. Our team works directly with homeowners to provide real, practical solutions tailored to your situation.</p>
    <p class="abs display tag light" style="top:203px;width:140px">No Pressure.</p>
    <p class="abs display tag gold" style="top:233px;width:153px">No Obligation.</p>
    <p class="abs display tag light" style="top:263px;width:223px">Just Honest Guidance.</p>
    <p class="abs licence">Marcus Fennimore is a Licensed Realtor with Copperleaf Homes Realty in Bethesda, Maryland.</p>
    <p class="abs display back-call">Call Now!<span>(240) 558-2094</span></p>
    <p class="abs contact-pill web">
      <svg width="13" height="13" viewBox="0 0 14 14" fill="none" stroke="#000" stroke-width="1.3"><circle cx="7" cy="7" r="6"/><ellipse cx="7" cy="7" rx="2.6" ry="6"/><path d="M1 7 H13"/></svg>
      www.hpbllc.com
    </p>
    <p class="abs contact-pill mail">
      <svg width="13" height="10" viewBox="0 0 13 10" fill="none" stroke="#fff" stroke-width="1.3"><rect x="0.7" y="0.7" width="11.6" height="8.6" rx="1.5"/><path d="M1.5 2 L6.5 5.6 L11.5 2"/></svg>
      marcus@hpbllc-mail.com
    </p>
    <p class="abs address">7200 Bramwick Lane Ellicott City, MD 21043</p>
  </div>
  <div class="abs city-strip" role="img" aria-label="Tall city towers beside a river at dusk"></div>

  <div class="abs stamp-box"></div>
  <div class="abs address-line" style="top:157px"></div>
  <div class="abs address-line" style="top:190px"></div>
  <div class="abs address-line" style="top:224px"></div>

  <div class="abs back-brand">
    <span class="brand-mark"></span>
    <span class="brand-name">Harbor Path<br>Partners LLC</span>
  </div>
</section>

</body>
</html>
```